Business Card Design Project (Beer industry)

I am seeking a redesign of my business card. I am looking for something that will really stand out in both texture and feel. Something more on the modern side then traditional. Nothing die cut shaped like a beer mug please.

The card is used mostly for other industry professionals, as well as bar and restaurant owners. My title is Strategy & Acquisitions. If you would like to somehow incorporate that theme, that may work.

My business is craft and imported beer. Nothing fizzy and yellow, so my products are more on the upscale side.
Updates

I was able to update my logo in .ai and .tif format. I hope that helps. 

Thank you all for your creative ideas. I have uploaded my current business card in pdf format, as well as our logo in .eps file format. We are excited about the submissions so far and want to thank you all again.

PS Please do not include fax number in future submissions, as we are looking for something more creative and a fax says 1999 and not 2015, which is the message we are going for, without being futuristic. 

Thank you all once again for all of your submissions. If we would consider a two sided card, we would like the opposite side not to be the same as the front. The styles we have seen so far, it appears the front and back are too similar. Again, a two sided card is not required. Thank you and we look forward to pushing the boundaries of your creativity. Cheers

Target Market(s)

My card would mostly go to bar and restaurant operators as well as other beer industry professionals

Industry/Entity Type

Restaurant

Requirements
Nice to have
• Two sided would be considered, although not required
Should not have
• Anything die cut shaped like a beer mug.

```html
<!DOCTYPE html>
<html lang="en">
<head>
<meta charset="utf-8">
<title>Holt Brew – Business Card</title>
<link rel="stylesheet" href="https://fonts.googleapis.com/css2?family=Noto+Serif:ital,wght@0,400;0,700;1,400&display=swap">
<style>
  :root {
    --page: #e6e0d4;
    --card: #f8f3e7;
    --wine: #8d1c22;
    --wine-dark: #6f1419;
    --gold: #d7a83a;
    --blue: #1f4f9c;
    --ink-grey: #6d6a64;
    --skyline-blue: #2a5aa8;
    --amber: #e7a62a;
  }
  * { margin: 0; padding: 0; box-sizing: border-box; }
  html, body {
    width: 1200px; height: 1023px; overflow: hidden;
    background: var(--page);
    font-family: "Noto Serif", Georgia, serif;
  }
  .card {
    position: absolute; left: 100px; top: 221px;
    width: 1000px; height: 580px;
    background: var(--card);
    border-radius: 22px;
    overflow: hidden;
    box-shadow: 0 6px 24px rgba(0,0,0,0.12);
  }
  .watermark {
    position: absolute; left: 40px; top: 30px;
    width: 420px; height: 380px;
    background: radial-gradient(ellipse at 50% 55%, rgba(31,79,156,0.07), rgba(31,79,156,0) 70%);
  }
  .person { position: absolute; left: 60px; top: 88px; }
  .person__name { color: var(--wine); font-size: 40px; font-weight: 400; line-height: 1.1; }
  .person__title { color: var(--ink-grey); font-size: 22px; margin-top: 6px; }
  .contact { position: absolute; left: 60px; top: 240px; color: var(--blue); }
  .contact__company { font-size: 22px; letter-spacing: 0.5px; }
  .contact__address { font-size: 22px; line-height: 1.35; margin-top: 12px; font-weight: 700; }
  .contact__lines { list-style: none; margin-top: 18px; font-size: 20px; line-height: 1.5; }
  .contact__lines li { display: flex; align-items: center; gap: 12px; }
  .contact__lines svg { width: 18px; height: 18px; fill: var(--blue); flex: none; }
  .brand {
    position: absolute; left: 520px; top: 40px; width: 440px;
    text-align: center;
  }
  .brand__art {
    width: 340px; height: 200px; margin: 0 auto;
    background: linear-gradient(180deg, #3a68b4 0%, var(--skyline-blue) 55%, #e9c46b 100%);
    border-radius: 8px 8px 0 0;
  }
  .brand__name {
    display: flex; align-items: center; justify-content: center; gap: 14px;
    margin-top: 14px;
    color: var(--wine); font-size: 50px; font-weight: 700; letter-spacing: 1px;
  }
  .brand__dot { width: 18px; height: 18px; border-radius: 50%; background: var(--wine); }
  .brand__city { color: var(--blue); font-size: 36px; font-style: italic; margin-top: 2px; }
  .brand__tagline { color: var(--ink-grey); font-size: 17px; font-style: italic; margin-top: 4px; }
  .band {
    position: absolute; left: 0; bottom: 0; width: 100%; height: 96px;
    background: linear-gradient(180deg, var(--wine), var(--wine-dark));
    border-top: 4px solid var(--gold);
    display: flex; align-items: center; justify-content: flex-end;
    padding-right: 120px;
  }
  .band__web { color: var(--gold); font-size: 28px; font-weight: 700; letter-spacing: 0.5px; }
</style>
</head>
<body>
  <main class="card">
    <div class="watermark" role="img" aria-label="Faint skyline and wheat decoration"></div>

    <section class="person">
      <h1 class="person__name">Daniel Reyes</h1>
      <p class="person__title">Sales Manager</p>
    </section>

    <section class="contact">
      <p class="contact__company">HOLT BREW CORP.</p>
      <p class="contact__address">42 Harbor Street<br>Brooklyn, New York 11201</p>
      <ul class="contact__lines">
        <li>
          <svg viewBox="0 0 24 24" aria-hidden="true"><path d="M6.6 10.8a15.1 15.1 0 0 0 6.6 6.6l2.2-2.2c.3-.3.7-.4 1-.2 1.1.4 2.3.6 3.6.6.6 0 1 .4 1 1V20c0 .6-.4 1-1 1A17 17 0 0 1 3 4c0-.6.4-1 1-1h3.5c.6 0 1 .4 1 1 0 1.3.2 2.5.6 3.6.1.3 0 .7-.2 1z"/></svg>
          (718) 555-0142
        </li>
        <li>
          <svg viewBox="0 0 24 24" aria-hidden="true"><path d="M7 2h10a2 2 0 0 1 2 2v16a2 2 0 0 1-2 2H7a2 2 0 0 1-2-2V4a2 2 0 0 1 2-2zm0 3v12h10V5zm5 13.5a1 1 0 1 0 0 2 1 1 0 0 0 0-2z"/></svg>
          (917) 555-0187
        </li>
        <li>
          <svg viewBox="0 0 24 24" aria-hidden="true"><path d="M3 5h18a1 1 0 0 1 1 1v12a1 1 0 0 1-1 1H3a1 1 0 0 1-1-1V6a1 1 0 0 1 1-1zm1 2.2V17h16V7.2l-8 5.3z M4.6 7 12 11.9 19.4 7z"/></svg>
          dreyes@example.com
        </li>
      </ul>
    </section>

    <section class="brand">
      <div class="brand__art" role="img" aria-label="Illustration of a city skyline with stars and a glass of beer"></div>
      <p class="brand__name"><span class="brand__dot"></span>HOLT BREW</p>
      <p class="brand__city">New York</p>
      <p class="brand__tagline">Premier Craft &amp; Import Beer Distributor</p>
    </section>

    <footer class="band">
      <span class="band__web">www.holtbrewco.com</span>
    </footer>
  </main>
</body>
</html>
```